Web site for mobile& web developers

We need a web site design for our company, Marlow Fenwick Studio Pty Ltd.

We are a Sydney based, software development company specialising in mobile platforms and web applications. We are a small, dynamic team with a few awesome products we want to get out to the world.

We would prefer a clean, professional layout that incorporates the company logo and branding; we do have a youthful, start-up edge which we would like to express.

We technical people with damn good products, so your design has to make us look good to non-technical people too!

Target Market(s)

B2B, Enterprise technology, Project Managers, Marketing, Other developers

Industry/Entity Type

It Company

Requirements
Must have
• Required pages:
- home page - this must allow us to feature our software (mobile & web) on the home page
- a standard content page (for things like "about us", "our team", etc)
- contact us (including HTML form with error state)
- mobile (iOS and Android) product page - allow for screen shots, features, requirements, customer list
- web product page - allow for screen shots, features, requirements, customer list

You must incorporate our logo and branding into the theme.
Should not have
• HTML/CSS carve is not required. We only required layered PNGs or PSDs.

```html
<!DOCTYPE html>
<html lang="en">
<head>
<meta charset="utf-8">
<title>Marlow Fenwick Studio</title>
<link rel="stylesheet" href="https://fonts.googleapis.com/css2?family=Noto+Sans:ital,wght@0,400;0,700;1,400&family=Squada+One&display=swap">
<style>
:root{
  --night:#1b262b;
  --mist:#ebebeb;
  --paper:#ffffff;
  --amber:#fbbd5c;
  --rust:#c0432b;
  --ink:#222222;
  --body:#4a4a4a;
  --slate:#7a7a7a;
  --link-blue:#1d5a8c;
  --sky-1:#dceef7;
  --sky-2:#8fbdd6;
  --sky-3:#3f6f8c;
}
*{margin:0;padding:0;box-sizing:border-box}
html,body{width:1200px;height:1007px;overflow:hidden}
body{position:relative;background:var(--mist);font-family:"Noto Sans",Verdana,sans-serif;color:var(--ink)}
.backdrop{position:absolute;left:0;top:0;width:1200px;height:1007px}
.footer-strip{position:absolute;left:0;top:996px;width:1200px;height:11px;background:var(--night)}

.brand{position:absolute;display:flex;align-items:center;gap:8px;color:var(--slate);font-weight:400;letter-spacing:2px}
.brand-dot{width:22px;height:22px;border-radius:50%;background:var(--amber)}
.brand--header{left:140px;top:80px;font-size:19px}
.brand--footer{left:236px;top:866px;font-size:17px}

.main-nav{position:absolute;top:61px;left:763px;display:flex;gap:0;font-size:13px}
.main-nav a{color:#fff;text-decoration:none;position:relative}
.main-nav a:nth-child(1){margin-right:31px}
.main-nav a:nth-child(2){margin-right:26px}
.main-nav a:nth-child(3){margin-right:29px}
.main-nav a.is-current::before{content:"";position:absolute;left:-3px;right:-4px;top:-8px;border-top:2px dotted #fff}

.page{position:absolute;left:134px;top:130px;width:933px;height:867px;background:var(--paper);box-shadow:0 0 6px rgba(0,0,0,.25)}

.hero{position:absolute;left:155px;top:151px;width:895px;height:336px}
.hero-visual{position:absolute;inset:0}
.hero-tagline{position:absolute;font-family:"Squada One",sans-serif;color:#fff;font-size:39px;line-height:1;text-shadow:0 0 2px #4d55a8,1px 1px 0 #4d55a8,-1px -1px 0 #4d55a8}
.hero-tagline--one{left:335px;top:162px}
.hero-tagline--two{left:523px;top:212px}
.hero-dots{position:absolute;right:49px;top:10px;display:flex;gap:8px}
.hero-dots span{width:10px;height:10px;border-radius:50%;background:#f4f4f4;box-shadow:0 0 2px rgba(0,0,0,.4)}
.hero-dots span:first-child{background:#cfcfcf}

.contact-card{position:absolute;left:155px;top:570px;width:285px;height:165px;background:var(--amber);box-shadow:4px 6px 5px rgba(0,0,0,.3)}
.contact-card h2{position:absolute;left:30px;top:16px;font-size:19px;font-weight:700}
.contact-card .phone{position:absolute;left:17px;top:63px;font-size:20px}
.contact-card .office{position:absolute;left:17px;top:95px;font-size:13px}
.contact-card .hiring{position:absolute;left:124px;top:122px;font-size:13px;font-weight:700;color:var(--link-blue)}
.contact-card .phone-icon{position:absolute;left:188px;top:8px;opacity:.22}

.intro{position:absolute;left:488px;top:567px;width:540px}
.intro h2{display:flex;align-items:center;gap:8px;font-size:16px;color:var(--rust);font-weight:700;margin-left:3px}
.intro p{font-size:14px;line-height:19px;color:var(--body);margin-top:6px}
.intro p + p{margin-top:19px}
.work-link{position:absolute;left:843px;top:766px;font-size:17px;font-style:italic;color:var(--rust);text-decoration:none}

.divider{position:absolute;left:153px;top:800px;width:895px;border-top:1px solid var(--rust)}

.footer-info{position:absolute;left:181px;top:910px;font-size:12.5px;line-height:23px}

.tab{position:absolute;width:246px;height:27px;background:var(--amber);box-shadow:3px 5px 4px rgba(0,0,0,.3);font-style:italic;font-size:16px;padding:3px 0 0 12px;color:var(--ink)}
.tab--feed{left:473px;top:830px}
.tab--social{left:768px;top:830px;padding-left:22px}

.feed{position:absolute;left:481px;top:917px;font-size:12.5px;line-height:28px}

.social{position:absolute;left:797px;top:956px;display:flex;gap:11px}
.social span{width:22px;height:22px;border-radius:50%;background:#8a8a8a;box-shadow:0 1px 2px rgba(0,0,0,.3)}
</style>
</head>
<body>
<svg class="backdrop" viewBox="0 0 1200 1007" aria-hidden="true">
  <path d="M0 0H1200V392Q1130 402 1067 400L134 400Q60 396 0 385Z" fill="var(--night)"/>
</svg>
<div class="footer-strip"></div>

<div class="brand brand--header"><span class="brand-dot"></span>MARLOW FENWICK</div>

<nav class="main-nav">
  <a href="#" class="is-current">About</a>
  <a href="#">News</a>
  <a href="#">Contact</a>
  <a href="#">Work with us</a>
</nav>

<div class="page"></div>

<section class="hero">
  <svg class="hero-visual" viewBox="0 0 895 336" preserveAspectRatio="none" role="img" aria-label="Globe map with light streaks in icy blue tones">
    <defs>
      <linearGradient id="heroSky" x1="0" y1="0" x2="1" y2="1">
        <stop offset="0" stop-color="var(--sky-2)"/>
        <stop offset=".45" stop-color="var(--sky-1)"/>
        <stop offset="1" stop-color="var(--sky-3)"/>
      </linearGradient>
    </defs>
    <path d="M0 0H895V318Q447 300 0 318Z" fill="url(#heroSky)"/>
  </svg>
  <div class="hero-dots"><span></span><span></span><span></span><span></span></div>
  <div class="hero-tagline hero-tagline--one">A world of solutions for a</div>
  <div class="hero-tagline hero-tagline--two">world without boundaries.</div>
</section>

<aside class="contact-card">
  <svg class="phone-icon" width="90" height="90" viewBox="0 0 90 90" aria-hidden="true">
    <path d="M14 18c6-6 12-6 16 0l8 12c3 5 1 9-3 12l-4 3c3 8 9 14 17 17l3-4c3-4 7-6 12-3l12 8c6 4 6 10 0 16-8 8-22 6-40-12S6 26 14 18Z" fill="var(--ink)"/>
    <path d="M50 22a20 20 0 0 1 18 18M52 8a34 34 0 0 1 30 30" stroke="var(--ink)" stroke-width="6" fill="none" stroke-linecap="round"/>
  </svg>
  <h2>Contact Us?</h2>
  <div class="phone">+61 2 9000 4127</div>
  <div class="office">Office location: Sydney, Australia</div>
  <div class="hiring">We are hiring!</div>
</aside>

<section class="intro">
  <h2>
    <svg width="24" height="18" viewBox="0 0 24 18" aria-hidden="true">
      <circle cx="8" cy="5" r="4" fill="var(--ink)"/><path d="M0 18c0-6 4-8 8-8s8 2 8 8Z" fill="var(--ink)"/>
      <circle cx="17" cy="5" r="3.5" fill="var(--ink)"/><path d="M13 11c1-1 3-1 4-1 4 0 7 2 7 8h-6c0-3-2-5-5-7Z" fill="var(--ink)"/>
    </svg>
    Who Are We?
  </h2>
  <p>We are passionate about quality products. Our core focus is on producing qual-ity user centric products from your ideas. Bleeding edge technologies, high-volume consumer digital products and knowing your audience are our bread and butter.</p>
  <p>We are the leading online and mobile technology BPO in the Asia Pacific region. We have the passion, the talent and the network to make your idea the next big thing.</p>
</section>
<a href="#" class="work-link">&rarr;&nbsp; Work for us...</a>

<div class="divider"></div>

<div class="brand brand--footer"><span class="brand-dot"></span>MARLOW FENWICK</div>
<div class="footer-info">
  Make good ideas GREAT Products.<br>
  Quick contact - hello@marlowfenwick.example<br>
  +61 2 9000 4127
</div>

<div class="tab tab--feed">Marlow Fenwick Feed</div>
<div class="feed">Loading latest post - follow us here<br>@marlowfenwickstudio</div>

<div class="tab tab--social">Hang with us</div>
<div class="social" aria-label="Social links"><span></span><span></span><span></span><span></span><span></span></div>
</body>
</html>
```